Redesign of Brightvale.com website

Our website was initially developed 6+ years ago and has been maintained by several different designers. As a result, it is overly complex, inconsistent format/layout and the content is not well structured/easy to navigate

We need the site redeveloped with a more modern look and feel, simpler content structure and ability to implement new/improved tools, such as: Dynamic Forms, Sales Funnels, Landing Pages, improved metadata of our pages and posts, improved SEO/Page ranking, etc.

We currently use SalesForce CRM, Constant Contact for marketing automation and SmartSheet forms. We are investigating Zapier for workflow integration which could extend to our website.

Our current website is developed in WordPress, ideally we will stick with this platform, but we’re happy to consider other CMS' if strongly recommended. We may decide to remove/consolidate some of the pages and/or content as part of this re-design.

We don't want to rebrand (ie change corporate logo, colours scheme etc) as part of this website redevelopment and it is critical that we don't lose our current Page Ranking, SEO rankings, backlink benefits, etc as part of this redevelopment.

Sites we like the feel/design of are: plorvista.com, quindlefax.com and tovalip.com

Target Market(s)

Corporate, Enterprise and Government B2B clients.

Coding

Coded - Design and coding required

Number of Pages Required

5+ page

Font styles to use
Sans Serif

Colors
ffffff
ec1f27

Requirements
Must have
• Must retain the majority of content on our existing website (although we may re-write some of it as part of this redesign process).
Nice to have
• See above "Project Description"
Should not have

```html
<!DOCTYPE html>
<html lang="en">
<head>
<meta charset="utf-8">
<title>Brightvale — Business Continuity</title>
<link href="https://fonts.googleapis.com/css2?family=Jost:wght@400;500&family=Poppins:ital,wght@0,300;0,400;0,500;1,300&display=swap" rel="stylesheet">
<style>
:root{
  --red:#e03f3b;
  --navy:#34365a;
  --ink:#1f1f24;
  --text:#3d3d44;
  --muted:#6c6c74;
  --dark:#3a3a3d;
  --footer:#1b1b1d;
  --white:#ffffff;
  --soft:#f5f5f6;
}
*{box-sizing:border-box;margin:0;padding:0}
html,body{width:1200px;height:4135px;overflow:hidden}
body{position:relative;background:var(--white);font-family:"Poppins",sans-serif;color:var(--text)}
.abs{position:absolute}
.heading{font-family:"Jost",sans-serif;font-weight:500;text-transform:uppercase;line-height:1.22;color:var(--ink)}
.heading .accent{color:var(--red)}
.btn{position:absolute;display:flex;align-items:center;justify-content:center;background:var(--red);color:var(--white);font-family:"Jost",sans-serif;font-size:18px;border-radius:40px;box-shadow:0 6px 14px rgba(224,63,59,.28)}
.art{position:absolute;border-radius:24px}

/* header */
.brand{left:172px;top:36px;display:flex;align-items:center;gap:10px;font-family:"Jost",sans-serif;font-weight:500;font-size:32px;color:var(--red)}
.brand-dot{width:26px;height:26px;border-radius:50%;background:var(--red)}
.nav{left:558px;top:57px;display:flex;gap:24px;font-family:"Jost",sans-serif;font-size:13px;color:var(--ink);letter-spacing:.3px}

/* hero */
.hero-title{left:172px;top:196px;font-size:48px;color:var(--navy);line-height:1.12}
.hero-sub{left:172px;top:330px;font-family:"Jost",sans-serif;font-size:23px;line-height:32px;color:var(--ink)}

/* services */
.section-title{width:1200px;text-align:center;font-size:37px}
.services-intro{left:200px;top:672px;width:800px;text-align:center;font-size:12.6px;line-height:25px;color:var(--text)}
.card{position:absolute;top:778px;width:256px;height:409px;background:var(--white);border-radius:0 0 42px 0;box-shadow:0 4px 18px rgba(0,0,0,.14);padding:34px 4px 0 51px}
.card::before{content:"";position:absolute;z-index:-1;top:-10px;right:-11px;left:20px;bottom:8px;border-radius:22px 22px 42px 0;background:var(--dark)}
.card.is-red::before{background:var(--red)}
.card-icon{position:absolute;left:-38px;top:39px;width:76px;height:76px;border-radius:50%;background:var(--white);border:2px solid var(--dark);display:flex;align-items:center;justify-content:center}
.card-icon::after{content:"";position:absolute;inset:5px;border-radius:50%;border:1px solid #c9c9cc}
.card.is-red .card-icon{border-color:var(--red)}
.card h3{font-family:"Jost",sans-serif;font-weight:500;font-size:22px;line-height:28px;text-transform:uppercase;color:var(--ink);margin-bottom:12px}
.card.is-red h3{color:var(--red)}
.card ul{list-style:none;font-family:"Jost",sans-serif;font-size:12.2px;line-height:21.8px;color:var(--muted);white-space:nowrap}
.card .more{position:absolute;left:51px;top:356px;font-family:"Jost",sans-serif;font-weight:500;font-size:17px;color:var(--ink)}
.card.is-red .more{color:var(--red)}

/* safety */
.safe-title{left:613px;top:1344px;font-size:37px;line-height:45px}
.safe-copy{left:613px;top:1493px;width:418px;font-size:12px;line-height:24.6px;text-align:justify;color:var(--text)}

/* testimonials */
.testi-title{left:173px;top:1844px;font-size:36px;line-height:44px}
.quote-mark{left:488px;top:1800px;font-family:"Jost",sans-serif;font-size:260px;line-height:1;color:#f7dedd}
.quote{left:173px;top:1962px;width:505px;font-size:12px;line-height:30px;font-style:italic;font-weight:300;color:var(--ink)}
.quote-by{left:173px;top:2062px;font-family:"Jost",sans-serif;font-size:16px;line-height:32px;color:var(--red)}

/* news */
.news-bg{left:0;top:2300px;width:1200px;height:1258px;background:linear-gradient(180deg,#fff 0%,var(--soft) 30%,#fbfbfb 70%,#fff 100%)}
.tab{position:absolute;left:172px;width:237px;height:58px;border-radius:29px;background:var(--dark);color:var(--white);font-family:"Jost",sans-serif;font-weight:500;font-size:17px;display:flex;align-items:center;padding-left:13px;text-transform:uppercase}
.tab.is-active{background:var(--red)}
.post{position:absolute;width:280px;height:436px;background:var(--white);box-shadow:0 2px 10px rgba(0,0,0,.12);padding:6px;text-align:center}
.post-image{height:196px;border-radius:2px}
.post h4{margin:34px 6px 0;font-family:"Jost",sans-serif;font-weight:500;font-size:15.5px;line-height:26px;text-transform:uppercase;color:var(--ink)}
.post .cat{margin-top:6px;font-size:12px;color:var(--red)}
.post p{margin:8px 14px 0;font-size:12px;line-height:24.5px;font-weight:300;color:var(--text)}

/* footer */
.footer{left:0;top:3558px;width:1200px;height:577px;background:var(--footer);color:var(--white)}
.map{left:172px;top:109px;width:401px;height:341px;background:linear-gradient(135deg,#eef0ea,#e1e6ee 55%,#cfe0f3);border-radius:2px}
.addr{position:absolute;display:flex;gap:14px}
.addr svg{flex:none;margin-top:2px}
.addr h5{font-family:"Jost",sans-serif;font-weight:500;font-size:17px;line-height:24px;margin-bottom:1px}
.addr p{font-size:12px;line-height:24.6px;font-weight:300}
.rule{left:172px;top:495px;width:856px;height:2px;background:#d8d8d8}
.copy{left:0;top:526px;width:1200px;text-align:center;font-size:12px;color:var(--white)}
.code{left:1071px;top:526px;font-size:12px;color:var(--white)}
</style>
</head>
<body>

<header>
  <div class="abs brand"><span class="brand-dot"></span>brightvale</div>
  <nav class="abs nav">
    <span>HOME</span><span>SERVICES</span><span>ABOUT</span><span>CLIENTS</span><span>RESOURCES</span><span>BLOG</span><span>CONTACT</span>
  </nav>
</header>

<section class="hero">
  <h1 class="abs heading hero-title">Business<br><span class="accent">Continuity</span></h1>
  <p class="abs hero-sub">How Robust is Your Continuity<br>Framework?</p>
  <a class="btn" style="left:172px;top:420px;width:144px;height:58px">Read More</a>
  <div class="art" role="img" aria-label="Illustration of an office team at a desk and sofa beneath wall clocks" style="left:585px;top:152px;width:562px;height:330px;background:linear-gradient(135deg,#fbe6e8,#f6c9cd 50%,#eef0f6)"></div>
</section>

<section class="services">
  <h2 class="abs heading section-title" style="left:0;top:610px">Our <span class="accent">Services</span></h2>
  <p class="abs services-intro">As an executive in any business, it is understandable that you want to ensure it is 100% safe, because your business is only as<br>strong as its weakest link.</p>

  <article class="card" style="left:172px">
    <div class="card-icon"><svg width="34" height="34" viewBox="0 0 34 34" fill="none" stroke="#3a3a3d" stroke-width="2"><rect x="7" y="4" width="20" height="26" rx="2"/><line x1="11" y1="11" x2="23" y2="11"/><line x1="11" y1="16" x2="23" y2="16"/><line x1="11" y1="21" x2="19" y2="21"/></svg></div>
    <h3>Resilience &amp;<br>Continuity</h3>
    <ul>
      <li>Business Continuity Management</li><li>Disaster Recovery Planning</li><li>Crisis Management</li><li>Emergency Management Planning</li><li>Workplace Health and Safety</li><li>Pandemic Response Planning</li><li>Risk Management</li><li>Strategy Development</li><li>Policy, Plan &amp; Process Development</li><li>Plan Testing and Exercising</li><li>Maintenance, Governance</li>
    </ul>
    <span class="more">READ MORE</span>
  </article>

  <article class="card is-red" style="left:478px">
    <div class="card-icon"><svg width="34" height="34" viewBox="0 0 34 34" fill="none" stroke="#e03f3b" stroke-width="2"><rect x="5" y="7" width="24" height="16" rx="2"/><line x1="2" y1="27" x2="32" y2="27"/><rect x="13" y="12" width="8" height="7" rx="1"/></svg></div>
    <h3>Security<br>Management</h3>
    <ul>
      <li>Digital Information Security Policy</li><li>Information Security Management</li><li>Cyber Security Awareness Training</li><li>Security Review and Assessment</li><li>Security Risk Management</li><li>Vulnerability Identification &amp;</li><li>Testing</li><li>Penetration Testing</li><li>Network Traffic Analysis</li>
    </ul>
    <span class="more">READ MORE</span>
  </article>

  <article class="card" style="left:784px">
    <div class="card-icon"><svg width="34" height="34" viewBox="0 0 34 34" fill="none" stroke="#3a3a3d" stroke-width="2"><circle cx="17" cy="17" r="6"/><circle cx="17" cy="17" r="12" stroke-dasharray="4 3"/></svg></div>
    <h3>IT Services &amp;<br>Solutions</h3>
    <ul>
      <li>Kestrel Recovery Planner (BCM</li><li>Software)</li><li>Tessel Mobile Incident Response</li><li>Application</li><li>Solution Design &amp; Implementation</li><li>IT Service Management (ITIL/ITSM)</li><li>IT Process &amp; Policy Development</li><li>IT Sourcing Strategy</li><li>StateDC Migration Strategy</li><li>Technology Refresh Strategy</li><li>ITIL Audits</li>
    </ul>
    <span class="more">READ MORE</span>
  </article>
</section>

<section class="safety">
  <div class="art" role="img" aria-label="Illustration of two people saving coins into a large jar" style="left:16px;top:1363px;width:569px;height:305px;background:linear-gradient(120deg,#f4f4f6,#f9dcdd 55%,#e9eaf2);border-radius:120px 120px 0 0"></div>
  <h2 class="abs heading safe-title">How to Ensure<br><span class="accent">Your Business is 100%<br>Safe</span></h2>
  <p class="abs safe-copy">You know that if you have a disastrous incident it will cause irreversible damage to your company's good name, your shareholders, board of directors and industry regulators. It will also cause severe legal ramifications. Sure, you can insure the physical assets of your business with an insurance policy, but it's not the desks, chairs and IT infrastructure that keeps you in business, it's your business processes and your staff.</p>
  <a class="btn" style="left:613px;top:1665px;width:117px;height:49px;font-size:16px">Read More</a>
</section>

<section class="testimonials">
  <h2 class="abs heading testi-title">Our<br><span class="accent">Testimonials</span></h2>
  <div class="abs quote-mark" aria-hidden="true">&rdquo;</div>
  <p class="abs quote">“The knowledge you’ve amassed about our IT environment in such as short space of time is incredible.&nbsp; We have been trying to develop this same knowledge internally for years, and you have done so in just a matter of weeks”</p>
  <p class="abs quote-by">Dana Whitlow, Executive Director IM&amp;T (CIO), State<br>Department of Civic Services</p>
  <a class="btn" style="left:173px;top:2154px;width:119px;height:50px;font-size:16px">Load More</a>
  <div class="art" role="img" aria-label="Illustration of a cheering team holding up thumbs-up signs" style="left:690px;top:1861px;width:510px;height:305px;background:linear-gradient(135deg,#f3f3f4,#f8d2d2 50%,#ececf1);border-radius:40px 0 0 140px"></div>
</section>

<section class="news">
  <div class="abs news-bg"></div>
  <h2 class="abs heading section-title" style="left:0;top:2346px;font-size:36px;line-height:44px">The Latest<br><span class="accent">News &amp; Information</span></h2>

  <div class="tab is-active" style="top:2557px">01. Business Continuity</div>
  <div class="tab" style="top:2632px">02. Disaster Recovery</div>
  <div class="tab" style="top:2707px">03. Pandemic</div>
  <div class="tab" style="top:2782px">04. View All</div>

  <article class="post" style="left:444px;top:2555px">
    <div class="post-image" role="img" aria-label="Photo of hands being washed under a tap" style="background:linear-gradient(135deg,#8d8f94,#c9c9cb 50%,#6f7277)"></div>
    <h4>COVID19 - Business Recovery Phase</h4>
    <div class="cat">Business Continuity, Pandemic</div>
    <p>The following is a summary of the status updates and actions in preparing for the Recovery Phase and addressing new risks which have been identified.</p>
  </article>

  <article class="post" style="left:747px;top:2555px">
    <div class="post-image" role="img" aria-label="Photo of network cables in a server rack" style="background:linear-gradient(135deg,#1e1e20,#6c6c70 50%,#2a2a2c)"></div>
    <h4>Decommissioning is part of Disaster Recovery Planning</h4>
    <div class="cat">Disaster Recovery</div>
    <p>More moving parts mean more chance of failure. Replace “moving parts” by “comatose IT servers” and the adage still holds true.</p>
  </article>

  <article class="post" style="left:444px;top:3019px">
    <div class="post-image" role="img" aria-label="Photo of a hand writing a phrase about change with a marker" style="background:linear-gradient(135deg,#e9e9e7,#cfd0cc 55%,#3a4a55)"></div>
    <h4>Adapt or Die - A Darwinian take on Business Continuity</h4>
    <div class="cat">Business Continuity</div>
    <p>Most businesses experience change constantly. Markets, technologies, regulations and strategies all evolve. Enterprises that stand.</p>
  </article>

  <article class="post" style="left:747px;top:3019px">
    <div class="post-image" role="img" aria-label="Photo of a person holding a phone over a city skyline" style="background:linear-gradient(135deg,#d5dde3,#8c99a4 55%,#2c3b4a)"></div>
    <h4>How’s your user experience for your disaster recovery?</h4>
    <div class="cat">Disaster Recovery</div>
    <p>It may sound strange to talk about “touchy-feely” stuff like user experience in the context of IT disaster recovery. After all, the priority is on getting systems.</p>
  </article>
</section>

<footer class="abs footer">
  <div class="abs map" role="img" aria-label="Street map showing the office location"></div>

  <div class="addr" style="left:617px;top:118px">
    <svg width="30" height="34" viewBox="0 0 30 34" fill="none" stroke="#fff" stroke-width="2.4"><path d="M15 32s11-10 11-18A11 11 0 0 0 4 14c0 8 11 18 11 18z"/><circle cx="15" cy="14" r="4"/></svg>
    <div>
      <h5>Street Address:</h5>
      <p>Brightvale Pty Ltd<br>Level 14, Tower 3 Harbour Point<br>88 Marlow Street<br>Easton NSW 2100<br>Australia</p>
    </div>
  </div>

  <div class="addr" style="left:866px;top:118px">
    <svg width="30" height="34" viewBox="0 0 30 34" fill="none" stroke="#fff" stroke-width="2.4"><path d="M15 32s11-10 11-18A11 11 0 0 0 4 14c0 8 11 18 11 18z"/><circle cx="15" cy="14" r="4"/></svg>
    <div>
      <h5>Postal Address:</h5>
      <p>PO Box 4270<br>Easton&nbsp; NSW&nbsp; 2101<br>Australia</p>
    </div>
  </div>

  <div class="addr" style="left:617px;top:283px">
    <svg width="30" height="34" viewBox="0 0 30 34" fill="none" stroke="#fff" stroke-width="2.4"><path d="M15 32s11-10 11-18A11 11 0 0 0 4 14c0 8 11 18 11 18z"/><circle cx="15" cy="14" r="4"/></svg>
    <div>
      <h5>Accountants:</h5>
      <p>Hollis Crane &amp; Partners<br>17 Finch Lane<br>Wrenfield NSW 2077</p>
    </div>
  </div>

  <div class="abs rule"></div>
  <p class="abs copy">Copyright © 2021 Brightvale. All Rights Reserved.</p>
  <span class="abs code">C20</span>
</footer>

</body>
</html>
```